Plum & Us Business Card Design

Plum & Us is a company that makes treats and real food for people with food allergies, illnesses and those that like to eat clean. We like to take good old fashioned favorites and create a clean, healthy version of it without losing any of the addictive ‘yumminess’ of it.All of our products are made with Organic ingredients and we aim to be as sustainable as possible therefore I would like this to be reflected in our business cards. I like the thought of using chia seeds in the business card maybe so that people could grow their own.

Industry/Entity Type

Health And Wellness

Contact Information for Business Card

Plum & Uswww.plumandus.com.aumarnie@plumandus.com.auP: 0431 596 218 Facebook and Instagram logos

Requirements
Must have
• Logo - does not have to be the exact logo as long as it is close and fits in with the other information I have asked for (sustainable & Organic, recycled etc.)
• See the photo with the treats for a picture of the logo

```html
<!DOCTYPE html>
<html lang="en">
<head>
<meta charset="utf-8">
<title>Plum &amp; Us – Business Card</title>
<link rel="stylesheet" href="https://fonts.googleapis.com/css2?family=Open+Sans:wght@400;600;700&display=swap">
<style>
  :root {
    --backdrop: #2e3034;
    --card: #ffffff;
    --navy: #27275f;
    --leaf: #1f6b2e;
    --stroke: #6f8f3c;
    --muted: #3d3d3d;
  }
  * { box-sizing: border-box; margin: 0; padding: 0; }
  html, body {
    width: 1200px; height: 864px; overflow: hidden;
    background: var(--backdrop);
    font-family: "Open Sans", Arial, sans-serif;
  }
  .sheet {
    position: relative; width: 1200px; height: 864px;
    display: flex; flex-direction: column; align-items: center;
    justify-content: center; gap: 40px;
  }
  .card {
    position: relative; width: 660px; height: 377px;
    background: var(--card); overflow: hidden;
    box-shadow: 0 6px 18px rgba(0,0,0,.35);
  }
  .wordmark {
    color: var(--navy); font-weight: 400; white-space: nowrap;
    letter-spacing: 1px;
  }
  .brush-line { position: absolute; height: 4px; background: var(--stroke); border-radius: 3px; opacity: .75; }

  /* front */
  .card--front .wordmark {
    position: absolute; left: 0; right: 0; top: 96px;
    text-align: center; font-size: 72px;
  }
  .card--front .brush-line { left: 150px; width: 360px; top: 200px; }
  .social { position: absolute; left: 0; right: 0; top: 262px; display: flex; justify-content: center; gap: 10px; }
  .social__dot { width: 22px; height: 22px; border-radius: 50%; background: var(--muted); }
  .card--front .brush-line--small { left: 290px; width: 80px; top: 300px; height: 2px; }

  /* back */
  .card--back .wordmark { position: absolute; left: 40px; top: 18px; font-size: 52px; }
  .card--back .brush-line { left: 40px; width: 270px; top: 98px; height: 3px; }
  .business-name { position: absolute; left: 58px; top: 166px; color: var(--leaf); font-weight: 700; font-size: 19px; }
  .contact { position: absolute; left: 44px; top: 222px; list-style: none; }
  .contact li { display: flex; align-items: center; gap: 10px; color: var(--navy); font-size: 15px; line-height: 22px; height: 22px; }
  .contact svg { width: 12px; height: 12px; fill: var(--leaf); flex: none; }
  .accent-ring {
    position: absolute; right: 40px; bottom: -40px; width: 280px; height: 280px;
    border: 7px solid var(--leaf); border-radius: 50%;
  }
</style>
</head>
<body>
<main class="sheet">
  <section class="card card--front" aria-label="Card front">
    <div class="wordmark">Plum &amp; Us</div>
    <div class="brush-line"></div>
    <div class="social" aria-label="Social links">
      <span class="social__dot"></span><span class="social__dot"></span>
    </div>
    <div class="brush-line brush-line--small"></div>
  </section>

  <section class="card card--back" aria-label="Card back">
    <div class="wordmark">Plum &amp; Us</div>
    <div class="brush-line"></div>
    <h1 class="business-name">Plum &amp; Us</h1>
    <ul class="contact">
      <li><svg viewBox="0 0 12 12"><path d="M2 1l2.2 0 1 2.6-1.3 1a6 6 0 0 0 3.5 3.5l1-1.3 2.6 1 0 2.2c-5 .5-9.5-4-9-9z"/></svg>0431 596 218</li>
      <li><svg viewBox="0 0 12 12"><path d="M0 2h12v8H0z M0 2l6 4 6-4" /></svg>marnie@plumandus.com.au</li>
      <li><svg viewBox="0 0 12 12"><circle cx="6" cy="6" r="6"/></svg>www.plumandus.com.au</li>
    </ul>
    <div class="accent-ring"></div>
  </section>
</main>
</body>
</html>
```